Healthcare IT company looking for business card design

We develop IT systems for healthcare that significantly reduces cost and improves quality.

We want a business card design that is professional and clean, and using the colors in our logo.

Doctors and decision makers in the healthcare industry

Healthcare

It should include
Name and title, address, telephone

Torvald Eskberg, CEO
+46 712 480517
torvald@velpamo.se

Serif

0355a3
ed282f

• Clean design
• Professional feel
• N/A
• N/A

```html
<!DOCTYPE html>
<html lang="en">
<head>
<meta charset="utf-8">
<title>Velpamo – Business Card</title>
<link href="https://fonts.googleapis.com/css2?family=Open+Sans:wght@400;600;700&display=swap" rel="stylesheet">
<style>
  :root {
    --brand-blue: #0355a3;
    --brand-red: #ed282f;
    --red-deep: #b81820;
    --ink-grey: #555a60;
    --rule-grey: #d4d6d9;
    --paper: #ffffff;
    --backdrop: #e9e7e3;
  }
  * { margin: 0; padding: 0; box-sizing: border-box; }
  html, body {
    width: 1200px; height: 950px; overflow: hidden;
    background: var(--backdrop);
    font-family: "Open Sans", Arial, sans-serif;
  }
  .stage {
    position: relative; width: 1200px; height: 950px;
  }
  .card {
    position: absolute; left: 250px; width: 700px; height: 400px;
    border-radius: 4px; overflow: hidden;
    box-shadow: 0 8px 24px rgba(0,0,0,.18);
  }
  /* Back side */
  .card--back {
    top: 50px;
    background: linear-gradient(120deg, var(--brand-red) 0%, #e1232a 55%, var(--red-deep) 100%);
  }
  .card--back .wordmark {
    position: absolute; left: 0; right: 0; top: 130px;
    text-align: center; color: var(--paper);
    font-size: 104px; font-weight: 700; letter-spacing: -1px; line-height: 1;
  }
  .card--back .web {
    position: absolute; left: 0; right: 0; top: 300px;
    text-align: center; color: rgba(255,255,255,.85);
    font-size: 18px; letter-spacing: 6px;
  }
  /* Front side */
  .card--front {
    top: 500px; background: var(--paper);
  }
  .card--front .bands { position: absolute; inset: 0; }
  .card--front .wordmark {
    position: absolute; left: 48px; top: 128px;
    color: var(--brand-blue);
    font-size: 62px; font-weight: 700; letter-spacing: -1px; line-height: 1;
  }
  .divider {
    position: absolute; left: 345px; top: 80px; width: 1px; height: 220px;
    background: linear-gradient(to bottom, transparent, var(--rule-grey) 20%, var(--rule-grey) 80%, transparent);
  }
  .contact {
    position: absolute; left: 372px; top: 98px; color: var(--ink-grey);
  }
  .contact .name {
    color: var(--brand-blue); font-size: 23px; font-weight: 600; line-height: 1.1;
  }
  .contact .title {
    color: var(--brand-red); font-size: 15px; margin-bottom: 14px;
  }
  .contact .address { font-size: 16px; line-height: 1.35; margin-bottom: 4px; }
  .contact .line {
    display: flex; align-items: center; gap: 8px; font-size: 16px; line-height: 1.5;
  }
  .contact .line svg { width: 15px; height: 15px; fill: var(--brand-blue); flex: none; }
  .card--front .web {
    position: absolute; left: 380px; right: 20px; top: 362px;
    text-align: center; color: var(--paper);
    font-size: 16px; letter-spacing: 6px;
  }
</style>
</head>
<body>
<main class="stage">
  <section class="card card--back" aria-label="Card back">
    <div class="wordmark">Velpamo</div>
    <div class="web">www.velpamo.se</div>
  </section>

  <section class="card card--front" aria-label="Card front">
    <svg class="bands" viewBox="0 0 700 400" width="700" height="400" aria-hidden="true">
      <polygon points="0,378 340,378 326,400 0,400" fill="var(--brand-red)"/>
      <polygon points="300,400 332,350 700,350 700,400" fill="var(--brand-blue)"/>
    </svg>

    <div class="wordmark">Velpamo</div>
    <div class="divider"></div>

    <div class="contact">
      <div class="name">Torvald Eskberg</div>
      <div class="title">CEO</div>
      <div class="address">2716 Harrowgate Lane<br>Elm Ridge, NY 11420</div>
      <div class="line">
        <svg viewBox="0 0 24 24"><path d="M6.6 10.8a15.1 15.1 0 0 0 6.6 6.6l2.2-2.2a1 1 0 0 1 1-.25 11.4 11.4 0 0 0 3.6.57 1 1 0 0 1 1 1V20a1 1 0 0 1-1 1A17 17 0 0 1 3 4a1 1 0 0 1 1-1h3.5a1 1 0 0 1 1 1c0 1.25.2 2.45.57 3.6a1 1 0 0 1-.25 1z"/></svg>
        <span>+46 712 480517</span>
      </div>
      <div class="line">
        <svg viewBox="0 0 24 24"><path d="M2 5h20v14H2z M3.5 6.5 12 13l8.5-6.5" fill="none" stroke="var(--brand-blue)" stroke-width="2"/></svg>
        <span>torvald@velpamo.se</span>
      </div>
    </div>

    <div class="web">www.velpamo.se</div>
  </section>
</main>
</body>
</html>
```